Seeking funky, innovative business cards

I am looking to refresh our current business cards to something more engaging, visual and impactful. We are a management consultancy firm, see website (www.larkspur-advisory.com.au). I've included our colour scheme, sample of the slides we use and our old business cards. We would like our cards to have icons. The card should display:- Name- Title- Mobile number- Address- Email address- Website - Company logo- Our purpose statement "We create the best places on earth to work"

Contact Information for Business Card

Tavish Brellan
Consultant
0491 672 348
Level 5, 218 Warrick Lane, Melbourne 3000
tavish@larkspur-advisory.com.au
www.larkspur-advisory.com.au

Purpose statement "we create the best places on earth to work"
LOGO available in google images

Font styles to use
Other font styles liked:
• Open Sans Light, Bebas Neue (open to other cool foints)

Colors
ffc214
5c5c5c
f5f5f5
fefefe

Requirements
Must have
• - Name
• - Title
• - Mobile number
• - Address
• - Email address
• - Website
• - Company logo
• - Our purpose statement "We create the best places on earth to work"
Nice to have
• - Icons
• - Colour (see our colour scheme"

```html
<!DOCTYPE html>
<html lang="en">
<head>
<meta charset="utf-8">
<title>Larkspur Advisory business cards</title>
<link rel="stylesheet" href="https://fonts.googleapis.com/css2?family=Lato:wght@400;700&family=Raleway:wght@400&display=swap">
<style>
  :root {
    --stage: #9c9d9f;
    --charcoal: #454849;
    --yellow: #ffc214;
    --ink: #3a3c3d;
    --paper: #fefefe;
    --muted: #5c5c5c;
  }
  * { box-sizing: border-box; margin: 0; padding: 0; }
  html, body { width: 1200px; height: 930px; overflow: hidden; }
  body {
    background: var(--stage);
    position: relative;
    font-family: "Lato", sans-serif;
  }
  .card {
    position: absolute;
    width: 600px;
    height: 343px;
    border-radius: 22px;
    overflow: hidden;
    box-shadow: 0 6px 14px rgba(0,0,0,.25);
  }
  .card--back { left: 70px; top: 80px; background: var(--charcoal); }
  .card--front { left: 530px; top: 490px; background: var(--paper); }

  .brand {
    position: absolute;
    display: flex;
    align-items: center;
    gap: 12px;
    font-family: "Raleway", sans-serif;
    font-weight: 400;
    letter-spacing: -1px;
  }
  .brand__dot {
    width: 12px; height: 12px; border-radius: 50%;
    background: var(--yellow);
  }
  .card--back .brand { left: 0; right: 0; top: 118px; justify-content: center; font-size: 54px; color: #fff; }
  .card--front .brand { right: 38px; top: 40px; font-size: 38px; color: var(--ink); }

  .tagline {
    position: absolute; left: 0; right: 0; bottom: 70px;
    text-align: center; color: var(--yellow); font-size: 19px;
  }

  .rule {
    position: absolute; height: 1px; background: var(--yellow);
  }
  .rule--top { left: 150px; right: 48px; top: 118px; }
  .rule--mid { left: 34px; right: 230px; top: 244px; }

  .person { position: absolute; left: 34px; top: 180px; }
  .person__name { color: var(--yellow); font-weight: 700; font-size: 27px; letter-spacing: 1.5px; text-transform: uppercase; }
  .person__title { color: var(--ink); font-size: 16px; margin-top: 2px; }

  .address {
    position: absolute; right: 48px; top: 132px;
    text-align: right; color: var(--ink); font-size: 15px; line-height: 1.35;
  }

  .contacts { position: absolute; left: 34px; top: 256px; list-style: none; }
  .contacts li {
    display: flex; align-items: center; gap: 10px;
    color: var(--ink); font-size: 15px; line-height: 19px;
  }
  .contacts svg { width: 12px; height: 12px; flex: none; }

  .corner { position: absolute; right: 0; bottom: 0; width: 150px; height: 230px; }
</style>
</head>
<body>
  <section class="card card--back" aria-label="Card back">
    <div class="brand"><span class="brand__dot"></span>Larkspur Advisory</div>
    <p class="tagline">Strategy. People. Impact.</p>
  </section>

  <section class="card card--front" aria-label="Card front">
    <div class="brand"><span class="brand__dot"></span>Larkspur Advisory</div>
    <div class="rule rule--top"></div>

    <p class="address">Level 2, 218 Warrick Lane<br>Melbourne, VIC 3000</p>

    <div class="person">
      <p class="person__name">Marlowe Tennant</p>
      <p class="person__title">Business Manager</p>
    </div>
    <div class="rule rule--mid"></div>

    <ul class="contacts">
      <li>
        <svg viewBox="0 0 12 12"><path d="M2.5 1l2 2.2-1 1.3c.7 1.5 2 2.8 3.5 3.5l1.3-1 2.2 2-1 1.6C5.8 10.4 1.6 6.2 1 1.9z" fill="var(--yellow)"/></svg>
        +61 3 9488 2063
      </li>
      <li>
        <svg viewBox="0 0 12 12"><rect x="1" y="4" width="10" height="6" rx="1" fill="var(--yellow)"/><rect x="3" y="1" width="6" height="3" fill="var(--yellow)"/></svg>
        +61 3 9715 3390
      </li>
      <li>
        <svg viewBox="0 0 12 12"><rect x="1" y="2.5" width="10" height="7" rx="1" fill="none" stroke="var(--yellow)" stroke-width="1.3"/><path d="M1.5 3l4.5 3.5L10.5 3" fill="none" stroke="var(--yellow)" stroke-width="1.3"/></svg>
        marlowe@larkspur-advisory.com.au
      </li>
      <li>
        <svg viewBox="0 0 12 12"><circle cx="6" cy="6" r="4.8" fill="none" stroke="var(--yellow)" stroke-width="1.2"/><path d="M1.2 6h9.6M6 1.2c-2.4 3-2.4 6.6 0 9.6M6 1.2c2.4 3 2.4 6.6 0 9.6" fill="none" stroke="var(--yellow)" stroke-width=".9"/></svg>
        www.larkspur-advisory.com.au
      </li>
    </ul>

    <svg class="corner" viewBox="0 0 150 230" aria-hidden="true">
      <path d="M150 40 C130 120 90 190 20 230 L150 230 Z" fill="var(--yellow)"/>
      <path d="M150 52 C133 128 98 194 34 230 L150 230 Z" fill="var(--charcoal)"/>
    </svg>
  </section>
</body>
</html>
```